Upscale dog care facility need some marketing material

We offer a lot of services for dogs and their humans. We have a large indoor dog park, swimming pools, dog daycare and boarding, Pet CPR/First Aid classes and training. We love the trifold brochures where we can highlight all of our services (even a few pics of the facility) as well as give everyone information on our pricing and membership concepts. Will primarily be used for marketing to vets and local pet stores to help get the word out about our business.

```html
<!DOCTYPE html>
<html lang="en">
<head>
<meta charset="utf-8">
<title>Splash &amp; Romp Trifold Brochure</title>
<link href="https://fonts.googleapis.com/css2?family=Alegreya+Sans:ital,wght@0,300;0,400;0,500;0,700;1,400&display=swap" rel="stylesheet">
<style>
  :root {
    --pool: #1b8cc0;
    --pool-deep: #0f6f9e;
    --pool-light: #5cc0e6;
    --ink: #3b3f44;
    --heading: #1f8bbf;
    --paper: #ffffff;
    --backdrop: #e6e7e9;
  }
  * { box-sizing: border-box; margin: 0; padding: 0; }
  html, body { width: 1200px; height: 2400px; overflow: hidden; }
  body {
    background: var(--backdrop);
    font-family: "Alegreya Sans", sans-serif;
    color: var(--ink);
    position: relative;
  }
  .spread {
    position: absolute;
    left: 40px;
    width: 1120px;
    height: 866px;
    background: var(--paper);
    box-shadow: 0 8px 30px rgba(0,0,0,.12);
    display: flex;
    overflow: hidden;
  }
  .spread--outside { top: 250px; }
  .spread--inside { top: 1284px; }
  .panel {
    position: relative;
    width: 373.33px;
    height: 100%;
    padding: 44px 34px;
    overflow: hidden;
  }
  .panel + .panel { border-left: 1px solid rgba(0,0,0,.05); }
  .section-title {
    font-weight: 400;
    text-transform: uppercase;
    color: var(--heading);
    font-size: 27px;
    letter-spacing: .5px;
    line-height: 1;
    margin-bottom: 10px;
  }
  .section-title--icon { display: flex; align-items: center; gap: 10px; }
  .icon-badge { width: 30px; height: 30px; flex: none; }
  .body-copy { font-size: 11.5px; line-height: 1.42; margin-bottom: 9px; }
  .body-copy--italic { font-style: italic; }
  .sub-title {
    font-weight: 400; text-transform: uppercase; color: var(--heading);
    font-size: 21px; line-height: 1; margin: 14px 0 6px;
  }
  .sub-title--small { font-size: 14px; margin: 12px 0 6px; }
  .tips { list-style: none; }
  .tips li {
    font-size: 10.5px; line-height: 1.35; padding-left: 18px; position: relative; margin-bottom: 5px;
  }
  .tips li svg { position: absolute; left: 0; top: 1px; width: 12px; height: 12px; }
  .photo { position: absolute; display: block; }
  .brand-name {
    font-family: "Alegreya Sans", sans-serif;
    font-weight: 500;
    color: var(--ink);
    font-size: 34px;
    line-height: 1;
    display: flex; align-items: center; gap: 10px;
  }
  .brand-name .dot { width: 14px; height: 14px; border-radius: 50%; background: var(--pool); }
  .brand-name--light { color: var(--paper); font-size: 30px; }
  .brand-name--light .dot { background: var(--paper); }

  /* outside middle (back) panel */
  .panel--back {
    background: linear-gradient(170deg, var(--pool-light) 0%, var(--pool) 40%, var(--pool-deep) 100%);
    color: var(--paper);
    text-align: center;
    padding-top: 70px;
  }
  .hours-label { font-weight: 700; text-transform: uppercase; font-size: 14px; letter-spacing: .4px; }
  .hours-value { font-size: 17px; font-weight: 300; margin-bottom: 14px; line-height: 1.25; }
  .map-area { display: block; margin: 18px auto 0; }
  .back-contact { position: absolute; left: 0; right: 0; bottom: 80px; text-align: center; }
  .back-contact .brand-name { justify-content: center; margin-bottom: 22px; }
  .contact-line { font-size: 17px; font-weight: 300; line-height: 1.35; }
  .contact-line + .contact-line { margin-top: 14px; }

  /* cover */
  .cover-brand { position: absolute; top: 60px; right: 40px; }
  .cover-headline {
    position: absolute; left: 34px; right: 34px; top: 640px;
    font-size: 40px; font-weight: 300; color: var(--heading); letter-spacing: 1.5px; line-height: 1;
  }
  .cover-tagline {
    position: absolute; left: 34px; right: 30px; top: 694px;
    font-size: 15px; line-height: 1.3; color: var(--ink);
  }
  .url-pill {
    position: absolute; left: 34px; right: 34px; top: 772px; height: 30px;
    background: var(--pool); color: var(--paper); border-radius: 15px;
    font-size: 14px; letter-spacing: 5px; text-align: center; line-height: 30px;
  }
  .story-photo-slot { position: absolute; left: 0; bottom: 0; }
</style>
</head>
<body>

<!-- OUTSIDE SPREAD -->
<section class="spread spread--outside">
  <div class="panel panel--story">
    <h2 class="section-title">Our Story</h2>
    <p class="body-copy body-copy--italic">Our dream of opening a pet care business started at the kitchen table. We found ourselves searching for a place close to home where our dogs could swim, run and play through every season, no matter how cold the winter or how hot the summer. When we could not find one, the answer was clear: build it ourselves and share it with everyone.</p>
    <p class="body-copy body-copy--italic">As the plans for our park grew, we asked what other services our community needed. Daycare, preschool and pool time soon joined the list, and Splash &amp; Romp was born!</p>
    <h2 class="section-title" style="margin-top:16px">Our Pledge to You</h2>
    <p class="body-copy body-copy--italic">We have lived and worked in the Fairview community for many years. Our passion for this town drives us every day to provide a safe, welcoming and joyful place for dogs and their families. Contact us any time to share what we are doing well or how we can serve you better!</p>
    <svg class="story-photo-slot" width="374" height="300" viewBox="0 0 374 300" role="img" aria-label="Photo of the owner family standing outdoors with their two dogs">
      <defs><linearGradient id="gForest" x1="0" y1="0" x2="1" y2="1"><stop offset="0" stop-color="#8a8f5c"/><stop offset="1" stop-color="#4e4a3c"/></linearGradient></defs>
      <path d="M0 60 C60 30 140 70 220 40 C290 15 350 20 374 50 L374 300 L0 300 Z" fill="url(#gForest)"/>
    </svg>
  </div>

  <div class="panel panel--back">
    <p class="hours-label">Working Hours</p>
    <p class="hours-value">7am–9pm (M–F) &amp; 9am–5pm (S–S)</p>
    <p class="hours-label">Dog Park Hours</p>
    <p class="hours-value">Tuesday – Friday: 10–1pm &amp; 4–8pm<br>Saturday/Sunday: 9–5pm</p>
    <svg class="map-area" width="230" height="150" viewBox="0 0 230 150" role="img" aria-label="Street map showing the facility location">
      <rect width="230" height="150" fill="#eef0f1"/>
    </svg>
    <div class="back-contact">
      <div class="brand-name brand-name--light"><span class="dot"></span>Splash &amp; Romp</div>
      <p class="contact-line">2210 Maple Grove Rd<br>Fairview IL, U.S.A. 60100</p>
      <p class="contact-line">555-014-2290</p>
      <p class="contact-line">www.splashandromp.com</p>
    </div>
  </div>

  <div class="panel panel--cover">
    <div class="brand-name cover-brand"><span class="dot"></span>Splash &amp; Romp</div>
    <svg class="photo" style="left:0;top:170px" width="374" height="450" viewBox="0 0 374 450" role="img" aria-label="Photo of a yellow Labrador swimming in a blue pool">
      <defs><linearGradient id="gPool" x1="0" y1="0" x2="1" y2="1"><stop offset="0" stop-color="#4fb6e4"/><stop offset="1" stop-color="#1e86c2"/></linearGradient></defs>
      <path d="M0 40 C60 10 120 60 190 30 C260 0 340 20 374 60 L374 420 C320 450 260 400 200 430 C130 460 60 420 0 440 Z" fill="url(#gPool)"/>
    </svg>
    <h1 class="cover-headline">POOL, PARK, FUN</h1>
    <p class="cover-tagline">Splash &amp; Romp is a place for dogs and their pet parents to enjoy time together in a safe, clean, comfortable environment that encourages interactive and healthy play.</p>
    <div class="url-pill">www.splashandromp.com</div>
  </div>
</section>

<!-- INSIDE SPREAD -->
<section class="spread spread--inside">
  <div class="panel panel--park">
    <svg class="photo" style="left:0;top:0" width="374" height="270" viewBox="0 0 374 270" role="img" aria-label="Photo of a small terrier running across green grass">
      <defs><linearGradient id="gGrass" x1="0" y1="0" x2="0" y2="1"><stop offset="0" stop-color="#6f8a3a"/><stop offset="1" stop-color="#9bbf4e"/></linearGradient></defs>
      <path d="M0 0 L374 0 L374 180 C320 230 260 200 200 240 C140 275 60 250 0 262 Z" fill="url(#gGrass)"/>
    </svg>
    <div style="margin-top:240px">
      <h2 class="section-title section-title--icon">
        <svg class="icon-badge" viewBox="0 0 30 30" aria-hidden="true"><circle cx="15" cy="15" r="14" fill="none" stroke="var(--heading)" stroke-width="2"/><path d="M7 20 L12 12 L15 17 L18 13 L23 20 Z" fill="var(--heading)"/></svg>
        Dog Park
      </h2>
      <p class="body-copy">Our indoor dog park is one of the first of its kind in the region. Our climate controlled space offers thousands of square feet of fenced-in fun, a cushioned floor that is easy on joints, and staff who watch over every play session. There will always be plenty of benches for you to sit on and observe the fun.</p>
      <p class="body-copy">Now Open! Over 2,500 square feet of outdoor space that you and your dog can access through the indoor park.</p>
      <p class="body-copy">Want to know who is visiting the park? Once you create your account, you can log in and see the live webcam of our park area. You'll never miss a chance to meet up with your 2 or 4-legged friends!</p>
      <h2 class="section-title section-title--icon" style="margin-top:18px">
        <svg class="icon-badge" viewBox="0 0 30 30" aria-hidden="true"><circle cx="15" cy="15" r="14" fill="none" stroke="var(--heading)" stroke-width="2"/><circle cx="15" cy="17" r="5" fill="var(--heading)"/><circle cx="9" cy="11" r="2.2" fill="var(--heading)"/><circle cx="21" cy="11" r="2.2" fill="var(--heading)"/><circle cx="15" cy="8" r="2.2" fill="var(--heading)"/></svg>
        Puppy Preschool
      </h2>
      <p class="body-copy">Play is a crucial part of a dog's development! The earlier a puppy is introduced to other puppies and different play styles in a positive setting, the quicker they learn how to play well. We offer preschool for puppies aged 10 to 24 weeks. Puppies must be up to date on vaccines, and small groups play under the eye of our trained staff. If play becomes too rough, a short time out helps everyone reset. Have questions? Contact us and let us know.</p>
    </div>
  </div>

  <div class="panel panel--pool">
    <h2 class="section-title section-title--icon">
      <svg class="icon-badge" viewBox="0 0 30 30" aria-hidden="true"><circle cx="15" cy="15" r="14" fill="none" stroke="var(--heading)" stroke-width="2"/><path d="M6 14 q3 -3 6 0 t6 0 t6 0 M6 19 q3 -3 6 0 t6 0 t6 0" fill="none" stroke="var(--heading)" stroke-width="2"/></svg>
      Dog Pool
    </h2>
    <p class="body-copy">Swimming is a great form of exercise that has long been used for animals and people alike. The water supports the body, eases pressure on joints, and builds strength and stamina. Dogs feel a sense of freedom in the water, and many find it calming. Whether your dog is recovering, aging or simply loves to splash, pool time can improve their quality of life.</p>
    <h3 class="sub-title">Make Pool Time<br>The Best Time</h3>
    <p class="body-copy">To make the most of your appointment, here are a few guidelines to follow:</p>
    <ul class="tips">
      <li><svg viewBox="0 0 12 12" aria-hidden="true"><circle cx="6" cy="7.5" r="3" fill="var(--heading)"/><circle cx="2.5" cy="4" r="1.3" fill="var(--heading)"/><circle cx="9.5" cy="4" r="1.3" fill="var(--heading)"/><circle cx="6" cy="2" r="1.3" fill="var(--heading)"/></svg>Be honest about the health of your dog. If you have any concerns, please discuss with your vet.</li>
      <li><svg viewBox="0 0 12 12" aria-hidden="true"><circle cx="6" cy="7.5" r="3" fill="var(--heading)"/><circle cx="2.5" cy="4" r="1.3" fill="var(--heading)"/><circle cx="9.5" cy="4" r="1.3" fill="var(--heading)"/><circle cx="6" cy="2" r="1.3" fill="var(--heading)"/></svg>Arrive 5-10 minutes prior to your swim time.</li>
      <li><svg viewBox="0 0 12 12" aria-hidden="true"><circle cx="6" cy="7.5" r="3" fill="var(--heading)"/><circle cx="2.5" cy="4" r="1.3" fill="var(--heading)"/><circle cx="9.5" cy="4" r="1.3" fill="var(--heading)"/><circle cx="6" cy="2" r="1.3" fill="var(--heading)"/></svg>Lightly brush your dog before entering the pool.</li>
      <li><svg viewBox="0 0 12 12" aria-hidden="true"><circle cx="6" cy="7.5" r="3" fill="var(--heading)"/><circle cx="2.5" cy="4" r="1.3" fill="var(--heading)"/><circle cx="9.5" cy="4" r="1.3" fill="var(--heading)"/><circle cx="6" cy="2" r="1.3" fill="var(--heading)"/></svg>Come in and watch. We encourage you to be poolside to cheer on your dog.</li>
      <li><svg viewBox="0 0 12 12" aria-hidden="true"><circle cx="6" cy="7.5" r="3" fill="var(--heading)"/><circle cx="2.5" cy="4" r="1.3" fill="var(--heading)"/><circle cx="9.5" cy="4" r="1.3" fill="var(--heading)"/><circle cx="6" cy="2" r="1.3" fill="var(--heading)"/></svg>Do not feed your dog for at least 2 hours before their swim.</li>
      <li><svg viewBox="0 0 12 12" aria-hidden="true"><circle cx="6" cy="7.5" r="3" fill="var(--heading)"/><circle cx="2.5" cy="4" r="1.3" fill="var(--heading)"/><circle cx="9.5" cy="4" r="1.3" fill="var(--heading)"/><circle cx="6" cy="2" r="1.3" fill="var(--heading)"/></svg>We have a drying room, but your dog may still be damp, so bring a towel.</li>
      <li><svg viewBox="0 0 12 12" aria-hidden="true"><circle cx="6" cy="7.5" r="3" fill="var(--heading)"/><circle cx="2.5" cy="4" r="1.3" fill="var(--heading)"/><circle cx="9.5" cy="4" r="1.3" fill="var(--heading)"/><circle cx="6" cy="2" r="1.3" fill="var(--heading)"/></svg>If you have any questions while your dog is in the pool, please ask!</li>
    </ul>
    <svg class="photo" style="left:0;bottom:0" width="374" height="250" viewBox="0 0 374 250" role="img" aria-label="Photo of a terrier wearing blue swim goggles lying on the floor">
      <defs><linearGradient id="gGoggle" x1="0" y1="0" x2="1" y2="1"><stop offset="0" stop-color="#d9d4cf"/><stop offset="1" stop-color="#8a6a4e"/></linearGradient></defs>
      <path d="M0 60 C80 20 160 40 240 20 C300 5 350 20 374 40 L374 250 L0 250 Z" fill="url(#gGoggle)"/>
    </svg>
  </div>

  <div class="panel panel--daycare">
    <h2 class="section-title section-title--icon">
      <svg class="icon-badge" viewBox="0 0 30 30" aria-hidden="true"><circle cx="15" cy="15" r="14" fill="none" stroke="var(--heading)" stroke-width="2"/><path d="M15 22 C6 16 8 9 12 9 C14 9 15 11 15 11 C15 11 16 9 18 9 C22 9 24 16 15 22 Z" fill="var(--heading)"/></svg>
      Dog Daycare
    </h2>
    <p class="body-copy">Welcome to Pup Academy, our full day doggie daycare! Here your dog spends the day in a small group, enjoying play time in the indoor park, rest breaks in a quiet room, and plenty of attention from our caring team. Dogs can even add a swim or a short lesson to their day for a little extra fun.</p>
    <p class="body-copy">We guarantee that your pup will come home tired, happy and maybe even a little smarter from their day at Pup Academy!</p>
    <svg class="photo" style="left:0;top:250px" width="374" height="300" viewBox="0 0 374 300" role="img" aria-label="Photo of a senior spaniel in a colourful life vest holding a toy">
      <defs><linearGradient id="gVest" x1="0" y1="0" x2="1" y2="1"><stop offset="0" stop-color="#c08a5a"/><stop offset="1" stop-color="#5c8fb8"/></linearGradient></defs>
      <path d="M40 30 C120 0 250 20 374 0 L374 260 C300 300 200 270 120 290 C70 300 20 280 0 250 L0 80 C10 55 20 40 40 30 Z" fill="url(#gVest)"/>
    </svg>
    <div style="position:absolute;left:34px;right:30px;top:568px">
      <h3 class="sub-title sub-title--small">What You Should Know About Pup Academy</h3>
      <ul class="tips">
        <li><svg viewBox="0 0 12 12" aria-hidden="true"><circle cx="6" cy="7.5" r="3" fill="var(--heading)"/><circle cx="2.5" cy="4" r="1.3" fill="var(--heading)"/><circle cx="9.5" cy="4" r="1.3" fill="var(--heading)"/><circle cx="6" cy="2" r="1.3" fill="var(--heading)"/></svg>Daycare is only offered Monday – Friday.</li>
        <li><svg viewBox="0 0 12 12" aria-hidden="true"><circle cx="6" cy="7.5" r="3" fill="var(--heading)"/><circle cx="2.5" cy="4" r="1.3" fill="var(--heading)"/><circle cx="9.5" cy="4" r="1.3" fill="var(--heading)"/><circle cx="6" cy="2" r="1.3" fill="var(--heading)"/></svg>A 15 minute park evaluation must be scheduled before your first day to make sure daycare is a good fit.</li>
        <li><svg viewBox="0 0 12 12" aria-hidden="true"><circle cx="6" cy="7.5" r="3" fill="var(--heading)"/><circle cx="2.5" cy="4" r="1.3" fill="var(--heading)"/><circle cx="9.5" cy="4" r="1.3" fill="var(--heading)"/><circle cx="6" cy="2" r="1.3" fill="var(--heading)"/></svg>Drop off is between 7am and 9am. Pick up is by 6pm.</li>
        <li><svg viewBox="0 0 12 12" aria-hidden="true"><circle cx="6" cy="7.5" r="3" fill="var(--heading)"/><circle cx="2.5" cy="4" r="1.3" fill="var(--heading)"/><circle cx="9.5" cy="4" r="1.3" fill="var(--heading)"/><circle cx="6" cy="2" r="1.3" fill="var(--heading)"/></svg>You are free to pick up any time before 6.</li>
        <li><svg viewBox="0 0 12 12" aria-hidden="true"><circle cx="6" cy="7.5" r="3" fill="var(--heading)"/><circle cx="2.5" cy="4" r="1.3" fill="var(--heading)"/><circle cx="9.5" cy="4" r="1.3" fill="var(--heading)"/><circle cx="6" cy="2" r="1.3" fill="var(--heading)"/></svg>There will be a late fee for picking up after 6pm.</li>
        <li><svg viewBox="0 0 12 12" aria-hidden="true"><circle cx="6" cy="7.5" r="3" fill="var(--heading)"/><circle cx="2.5" cy="4" r="1.3" fill="var(--heading)"/><circle cx="9.5" cy="4" r="1.3" fill="var(--heading)"/><circle cx="6" cy="2" r="1.3" fill="var(--heading)"/></svg>You can bring lunch for your dog in a bag labeled with their name.</li>
        <li><svg viewBox="0 0 12 12" aria-hidden="true"><circle cx="6" cy="7.5" r="3" fill="var(--heading)"/><circle cx="2.5" cy="4" r="1.3" fill="var(--heading)"/><circle cx="9.5" cy="4" r="1.3" fill="var(--heading)"/><circle cx="6" cy="2" r="1.3" fill="var(--heading)"/></svg>We have a 24 hour cancellation policy; a full day charge applies if cancelled later.</li>
      </ul>
    </div>
  </div>
</section>

</body>
</html>
```